Airport Advertising Brochure

I need a flyer put together asap! Previous example included. Would like something clean and updated. New logo and updated company name. I would like this designed in Pages or Illustrator so I can update content when needed. Website: pagelantern.com

Target Market(s)

Authors. This page has some good content about what we do: https://www.pagelantern.com/terminaladvertising/

Industry/Entity Type

Airport

Font styles to use
Serif
Sans Serif

Requirements
Must have
• Clean, modern design.

```html
<!DOCTYPE html>
<html lang="en">
<head>
<meta charset="utf-8">
<title>PageLantern — Terminal Advertising Brochure</title>
<link href="https://fonts.googleapis.com/css2?family=Archivo+Black&family=Roboto:wght@400;500;700&display=swap" rel="stylesheet">
<style>
  :root {
    --bg: #bcdcdf;
    --yellow: #f2cf1f;
    --black: #161616;
    --paper: #f3f2ee;
    --ink: #1d1d1d;
    --gold: #d9ab12;
    --muted: #6a6a6a;
    --photo-light: #e4e3df;
    --photo-mid: #b9bcbf;
  }
  * { box-sizing: border-box; margin: 0; padding: 0; }
  html, body { width: 1200px; height: 699px; overflow: hidden; }
  body {
    background: var(--bg);
    font-family: "Roboto", Arial, sans-serif;
    color: var(--ink);
    display: grid;
    grid-template-columns: 600px 600px;
    grid-template-rows: 349px 350px;
  }
  .panel { display: flex; align-items: center; justify-content: center; }

  .spread { display: flex; box-shadow: 0 10px 22px rgba(0,0,0,.18); }
  .page { position: relative; width: 250px; height: 172px; }
  .page--black { background: var(--black); }
  .page--yellow { background: var(--yellow); }
  .sheet { position: absolute; background: var(--paper); display: flex; overflow: hidden; }
  .page--left .sheet { top: 8px; left: 8px; bottom: 8px; right: 0; }
  .page--right .sheet { top: 8px; right: 8px; bottom: 8px; left: 0; }

  .cover { position: relative; width: 340px; height: 234px; background: var(--yellow); box-shadow: 0 10px 22px rgba(0,0,0,.18); }
  .cover .sheet { top: 11px; left: 11px; right: 11px; bottom: 11px; }

  .copy { position: relative; flex: 0 0 46%; padding: 14px 10px 8px 12px; }
  .copy--wide { flex: 1 1 auto; }
  .photo { flex: 1 1 auto; }
  .photo--terminal { background: linear-gradient(160deg, var(--photo-light) 0%, #f7f7f5 40%, var(--photo-mid) 100%); }
  .photo--store { background: linear-gradient(170deg, #c8c5a0 0%, #9a9783 55%, #ccc8b7 100%); }
  .photo--hall { background: linear-gradient(165deg, #d4d8d8 0%, #8fa091 45%, #b07f7a 100%); }
  .photo--collage { background: linear-gradient(150deg, #b98a55 0%, #7c6a5c 50%, #c29c87 100%); }
  .photo--shelves { background: linear-gradient(150deg, #d8b23c 0%, #6f7aa4 50%, #9e5a4e 100%); }

  .lead { font-size: 9px; line-height: 1.35; font-weight: 500; }
  .cover-lead { font-size: 10px; line-height: 1.35; font-weight: 500; margin-top: 20px; }
  .cover-list { font-size: 10px; line-height: 1.35; font-weight: 500; }
  .list { list-style: none; margin-top: 2px; }
  .list li::before { content: "• "; }

  .heading { font-family: "Archivo Black", "Arial Black", sans-serif; font-size: 10px; line-height: 1.05; text-transform: uppercase; }
  .heading--long { font-size: 8px; }
  .overview { font-size: 6.5px; margin-top: 3px; line-height: 1.3; }
  .fine { font-size: 4.5px; line-height: 1.35; margin-top: 2px; color: var(--muted); }
  .fine b { color: var(--ink); }
  .copy--mid { padding-top: 60px; }

  .brand { position: absolute; left: 12px; bottom: 8px; }
  .brand__row { display: flex; align-items: center; gap: 4px; }
  .brand__mark { width: 8px; height: 8px; background: var(--gold); }
  .brand__name { font-size: 9px; font-weight: 500; color: var(--gold); }
  .brand__url { font-size: 4.5px; margin-top: 1px; }
  .cover .brand { left: 14px; bottom: 10px; }
  .cover .brand__mark { width: 10px; height: 10px; }
  .cover .brand__name { font-size: 12px; }
  .cover .brand__url { font-size: 5.5px; }
</style>
</head>
<body>

  <section class="panel">
    <article class="cover">
      <div class="sheet">
        <div class="copy">
          <p class="cover-lead">Comprehensive Window Display, Front Table Placement, and Business Center Pockets.</p>
          <ul class="cover-list list"><li>45 Airports</li><li>2 Train Stations</li><li>80 Bookstores</li></ul>
          <div class="brand"><div class="brand__row"><span class="brand__mark"></span><span class="brand__name">PageLantern</span></div><p class="brand__url">www.pagelantern.com</p></div>
        </div>
        <div class="photo photo--terminal" role="img" aria-label="Bright white airport terminal hall with curved ceiling and travelers"></div>
      </div>
    </article>
  </section>

  <section class="panel">
    <div class="spread">
      <div class="page page--black page--left">
        <div class="sheet">
          <div class="copy copy--wide">
            <h2 class="heading">Destination Airports and NYC Train Stations</h2>
            <p class="fine"><b>Atlanta, GA – City International Airport</b><br>11 Bookstores</p>
            <div class="brand"><div class="brand__row"><span class="brand__mark"></span><span class="brand__name">PageLantern</span></div></div>
          </div>
        </div>
      </div>
      <div class="page page--yellow page--right">
        <div class="sheet">
          <div class="copy">
            <p class="lead" style="font-size:7px">Comprehensive Window Display, Front Table Placement, and Business Center Pockets.</p>
            <ul class="lead list" style="font-size:6px"><li>45 Airports</li><li>2 Train Stations</li><li>80 Bookstores</li></ul>
            <div class="brand"><div class="brand__row"><span class="brand__mark"></span><span class="brand__name">PageLantern</span></div><p class="brand__url">www.pagelantern.com</p></div>
          </div>
          <div class="photo photo--terminal" role="img" aria-label="Bright white airport terminal hall with travelers"></div>
        </div>
      </div>
    </div>
  </section>

  <section class="panel">
    <div class="spread">
      <div class="page page--black page--left">
        <div class="sheet">
          <div class="copy copy--mid">
            <h2 class="heading">Business Center Pocket</h2>
            <p class="overview">Overview:<br>1 month in 28 bookstores</p>
            <div class="brand"><div class="brand__row"><span class="brand__mark"></span><span class="brand__name">PageLantern</span></div><p class="brand__url">www.pagelantern.com</p></div>
          </div>
          <div class="photo photo--store" role="img" aria-label="Airport bookstore entrance with a book pocket rack"></div>
        </div>
      </div>
      <div class="page page--yellow page--right">
        <div class="sheet">
          <div class="copy">
            <h2 class="heading heading--long">Window Display, Front Table Display and Business Center Pockets</h2>
            <p class="fine"><b>Front Store Table Placement</b><br>Titles sit on the front table in busy terminal stores where travelers browse.</p>
            <p class="fine"><b>Window Display</b><br>Covers face the concourse for every passing traveler.</p>
            <p class="fine"><b>Business Center Pocket</b><br>Copies rest in business center racks near the gates.</p>
            <div class="brand"><div class="brand__row"><span class="brand__mark"></span><span class="brand__name">PageLantern</span></div></div>
          </div>
          <div class="photo photo--hall" role="img" aria-label="Busy airport concourse with crowds and a green tree"></div>
        </div>
      </div>
    </div>
  </section>

  <section class="panel">
    <div class="spread">
      <div class="page page--black page--left">
        <div class="sheet">
          <div class="copy copy--mid">
            <h2 class="heading">Window Display</h2>
            <p class="overview">Overview:<br>3 months in 28 bookstores</p>
            <div class="brand"><div class="brand__row"><span class="brand__mark"></span><span class="brand__name">PageLantern</span></div><p class="brand__url">www.pagelantern.com</p></div>
          </div>
          <div class="photo photo--collage" role="img" aria-label="Collage of bookstore window displays in terminals"></div>
        </div>
      </div>
      <div class="page page--yellow page--right">
        <div class="sheet">
          <div class="copy">
            <h2 class="heading heading--long" style="margin-top:8px">Front Store Table Display</h2>
            <p class="overview">Overview:<br>1 month in 28 bookstores</p>
            <div class="brand"><div class="brand__row"><span class="brand__mark"></span><span class="brand__name">PageLantern</span></div><p class="brand__url">www.pagelantern.com</p></div>
          </div>
          <div class="photo photo--shelves" role="img" aria-label="Colorful front store book tables and shelves"></div>
        </div>
      </div>
    </div>
  </section>

</body>
</html>
```